Legal Recruitment Firm Needs Wordpress Design

We are a legal recruitment firm that represents partner-level attorneys in the top 200 law firms in the world in their move from one law firm to another. I am the founder, and am a twice published author, and I write a column for Civic Counsel and Telvane.

My site will have 6 "pages" -- Who We Are | What We Do | How We Do It | Why We Are Different | About Our Founder | Contact Us -- and a blog (where I can post my Telvane interviews).

I have attached my logo, and expect that the color/design will follow from that. Where colors are concerned, I like blacks, grays, reds, deep blues, etc.

I'd like to use the Ortolan Studio theme -- http://plumewix.com/demo/ortolan-studio/

It is fairly simple, I like the full width page display, and I really like the video that plays in the background rather than just a static picture. So I’d like to have a video like this, but perhaps one made of short clips of the streets of NY, London, Hong Kong, etc. (We service attorneys around the world). It wouldn't have to be that, specifically, however -- I will leave the creative aspect up to you.

Please note: (i) I haven't purchased the theme as of yet, so I don't HAVE to use that theme. One that is comparable will do just as fine. Also, (ii) I don't want the typical stock photos of "business people." I really want this to look professional, and think that the stock photos of business people look cheap -- you know, the business websites of the 90's look.

Any photos we would use would have to be fresh, contemporary, and of high quality.

Below are the other themes that I like, and why I like them. I think this will help you to better understand the look/feel that I would like to achieve.

http://plumewix.com/demo/ortolan-studio/
-- This is a beautiful theme. And I really like the video in the beginning. I'd love to have a video like this for my page. Perhaps video of the streets of New York, Hong Kong, London, etc? Rather than just a static picture, a video like this?

http://skins.vardolite7.com/?theme=SnapKit
-- This is another very beautiful theme. I like -- very much -- the simplicity of the blog. The picture is beautiful. I don't think that the picture really caters to my business/industry, but it is amazing. I like the sprawling picture, the easy to follow menu, etc.

http://skinmarket.net/item/brisk-versatile-multiuse-wordpress-skin/full_screen_preview/58214067
-- Another beautiful theme. I really like the sprawling picture. I like the color pallette, as the white letters contrast nicely against it. The menu looks simple. In particular, as you scroll down, I like the video of the New York traffic -- it really adds to the quality, I think.

http://previewwp.qulbadesigns.com/tor/
I like the very clean look of this theme. Only one menu, and that menu only navigates to a single place on the site. The big, full screen, sprawling picture is great, and the font is great. I like the contrast of the white letters against the picture.

http://www.stylevantor.com/strings/
-- Not necessarily a great site, but I do like the full-screen picture, and i like the black/gray. I don't like the fonts. I like block lettering with clean, square lines.

http://demo.skinbriar.com/layerglide-two/
-- I like the big sprawling picture. The colors aren't bad. I like the white contrasting letters. I like that when you scroll down, there is good, clean division between the sections. The clip art of the people looks like, well, clip art. The polished people in suits just looks bad. I really don't like that. The photos should look fresh, contemporary, high def., etc.

http://skinmarket.kovatheme.com/wpversions/marrowby/landing/
-- I like the look of the landing page. This is mainly earth colors -- browns -- which, I want mine to follow the colors of my logo (or contrast in an intelligent way), but I like the big sprawling picture, and the white letters. I like as you scroll down that the division between the sections is more prominent -- you know when you are in a particular "section."

http://demo.brightvale-skins.com/otter/
-- I like the look of the landing page, but as you scroll down, it becomes too busy. This may just be because of the content they've put in, though.

Target Market(s)

Partner-level attorneys at the top 200 law firms in the world.

Industry/Entity Type

Law Firm

Number of Pages Required

5+ page

Font styles to use
Sans Serif

Requirements
Must have
• This will be the customization of an existing Wordpress theme, so I expect to receive that -- not simply an adobe mock up.
• Block-style fonts with square edges.
Nice to have
• I've included a significant amount of information in the job description.
Should not have
• Cheap-looking stock photos.

```html
<!DOCTYPE html>
<html lang="en">
<head>
<meta charset="utf-8">
<title>Keystone Meridian Partner Management</title>
<link href="https://fonts.googleapis.com/css2?family=Roboto:wght@400;500;700&family=Roboto+Condensed:wght@400;700&display=swap" rel="stylesheet">
<style>
:root{
  --black:#141414;
  --nav:#231f1d;
  --red:#c8161d;
  --blue:#1346b4;
  --title-blue:#1f4fb0;
  --gray-bg:#efefef;
  --light-bg:#f4f4f4;
  --text:#555;
  --dark:#333;
  --white:#fff;
}
*{box-sizing:border-box;margin:0;padding:0}
html,body{width:1200px;height:4905px;overflow:hidden}
body{font-family:'Roboto',sans-serif;color:var(--text);background:var(--white);font-size:14px;line-height:1.75}
.section-title{font-family:'Roboto Condensed',sans-serif;font-weight:700;font-size:24px;color:var(--title-blue);letter-spacing:.5px;text-transform:uppercase}
.btn{display:inline-block;border:1px solid #ccc;color:var(--red);font-family:'Roboto Condensed',sans-serif;font-weight:700;font-size:14px;text-transform:uppercase;text-align:center;background:var(--white);line-height:52px;height:54px;width:160px}
.photo{display:block}

/* header */
.top-bar{height:105px;background:var(--black);display:flex;align-items:center;justify-content:space-between;padding:0 75px 0 75px}
.brand{display:flex;align-items:center;gap:14px}
.brand-mark{width:46px;height:46px;background:var(--red)}
.brand-name{font-family:'Roboto Condensed',sans-serif;font-weight:700;font-size:30px;color:var(--white);line-height:1;text-transform:uppercase}
.social{display:flex;gap:14px}
.social span{width:38px;height:38px;border:2px solid #888;border-radius:50%;display:block}
.main-nav{height:58px;background:var(--nav);display:flex;align-items:center;padding-left:100px;gap:40px}
.main-nav a{color:var(--white);text-decoration:none;font-family:'Roboto Condensed',sans-serif;font-weight:700;font-size:14px;text-transform:uppercase}
.main-nav a.current{color:var(--red)}

/* hero */
.hero{position:relative;height:582px;background:linear-gradient(180deg,#b59a7a 0%,#8a6b4f 45%,#3b2e27 80%,#1e1a18 100%);text-align:center}
.hero-content{position:absolute;top:170px;left:0;right:0}
.hero-title{font-family:'Roboto Condensed',sans-serif;font-weight:700;font-size:92px;line-height:1;color:var(--red)}
.hero-sub{font-family:'Roboto Condensed',sans-serif;font-size:34px;color:var(--black);line-height:1.2;margin-top:6px;text-transform:uppercase}
.hero-lead{font-size:26px;color:var(--white);line-height:1.4;margin:14px auto 0;width:780px}

/* welcome */
.welcome{height:262px;text-align:center;padding-top:58px}
.welcome p{width:1050px;margin:24px auto 0;font-size:13px;line-height:1.9}

/* split */
.split{display:flex;height:488px}
.split .photo{width:600px;height:100%}
.split-text{width:600px;height:100%;padding:0 75px;display:flex;flex-direction:column;justify-content:center}
.split-text.gray{background:var(--gray-bg)}
.split-text p{margin:22px 0 28px;font-size:13px;line-height:1.9}
.what{height:480px}

/* how */
.how{height:896px;text-align:center;padding-top:58px}
.how-grid{display:grid;grid-template-columns:repeat(3,300px);column-gap:70px;row-gap:38px;justify-content:center;margin-top:48px}
.step svg{width:44px;height:44px}
.step h3{font-family:'Roboto Condensed',sans-serif;font-weight:700;color:var(--red);font-size:18px;text-transform:uppercase;margin-top:16px;line-height:1.3}
.step p{font-size:13px;line-height:1.8;margin-top:4px}
.how .btn{width:510px;margin-top:40px}

/* different */
.different{height:415px;background:var(--blue);color:var(--white);display:flex;align-items:center;padding:0 78px 0 75px;justify-content:space-between}
.different .section-title{color:var(--white)}
.different-text{width:545px}
.different-text p{font-size:13px;line-height:1.9;margin-top:16px}
.different .btn{background:transparent;color:var(--white);border-color:var(--white);margin-top:30px}
.different .photo{width:445px;height:310px}

/* founder */
.founder{height:435px;background:var(--gray-bg);display:flex}
.founder .photo{width:458px;height:100%}
.founder-text{padding:58px 60px 0 65px;width:742px}
.founder-text p{font-size:13px;line-height:1.9;margin:16px 0 30px}

/* blog */
.blog{height:465px;text-align:center;padding-top:50px;position:relative}
.blog-post{display:flex;text-align:left;margin:42px 0 0 98px;gap:32px}
.blog-post .photo{width:392px;height:272px}
.post-body{width:590px}
.post-title{font-family:'Roboto Condensed',sans-serif;font-weight:700;color:var(--red);font-size:18px;text-transform:uppercase}
.post-meta{font-size:10px;color:#888;margin-top:2px}
.post-body p{font-size:13px;line-height:1.8;margin:8px 0 24px}
.arrow{position:absolute;top:245px}
.arrow.left{left:55px}.arrow.right{right:55px}

/* contact */
.contact{height:497px;background:var(--light-bg);text-align:center;padding-top:48px}
.contact-form{width:514px;margin:42px auto 0;display:flex;flex-direction:column;gap:12px}
.field{background:var(--white);height:56px;text-align:left;padding:0 18px;font-size:13px;color:#888;line-height:56px}
.field.message{height:120px;line-height:1;padding-top:18px}
.send{height:54px;background:var(--red);color:var(--white);font-family:'Roboto Condensed',sans-serif;font-weight:700;font-size:14px;line-height:54px;text-transform:uppercase;margin-top:4px}

/* footer */
.footer{height:222px;background:var(--black);color:#ccc;font-size:14px}
.footer-info{display:flex;justify-content:space-between;padding:40px 150px 28px 160px;border-bottom:1px solid #333}
.footer-info span{display:flex;align-items:center;gap:12px}
.copyright{text-align:center;font-size:11px;color:#888;padding-top:36px}
</style>
</head>
<body>

<header>
  <div class="top-bar">
    <div class="brand">
      <span class="brand-mark"></span>
      <span class="brand-name">Keystone Meridian</span>
    </div>
    <div class="social" aria-label="Social links">
      <span></span><span></span><span></span><span></span>
    </div>
  </div>
  <nav class="main-nav">
    <a class="current" href="#">Home</a>
    <a href="#">Who We Are</a>
    <a href="#">What We Do</a>
    <a href="#">How We Do It</a>
    <a href="#">Why We Are Different</a>
    <a href="#">About Our Founder</a>
    <a href="#">Contact Us</a>
  </nav>
</header>

<section class="hero" role="img" aria-label="City street at dusk with a clock tower and government buildings, people crossing a bridge">
  <div class="hero-content">
    <h1 class="hero-title">KEYSTONE MERIDIAN</h1>
    <div class="hero-sub">Partner Management</div>
    <p class="hero-lead">We are a group of placement professionals who have made it our business to be experts in the business of law.</p>
  </div>
</section>

<section class="welcome">
  <h2 class="section-title">Welcome to our company</h2>
  <p>We place partner-level attorneys with the leading law firms of the world, and we take the time to learn each practice, each book of business and each ambition before a single call is made. Our approach is discreet, careful and measured, and we stay with every partner from the first meeting through the final transition into the new firm.</p>
</section>

<section class="split">
  <div class="photo" role="img" aria-label="Team of professionals in dark suits standing in an office" style="background:linear-gradient(135deg,#8a6a4c,#3d2d24 60%,#1d1a1a)"></div>
  <div class="split-text gray">
    <h2 class="section-title">Who we are</h2>
    <p>We are a group of placement professionals who have made it our business to be experts in the business of law. This means having a strong working knowledge in the following areas.</p>
    <a class="btn" href="#">Read more</a>
  </div>
</section>

<section class="split what">
  <div class="split-text">
    <h2 class="section-title">What we do</h2>
    <p>We are a boutique partner placement firm. In lay terms, we are legal recruiters. But where your traditional legal recruitment firm aligns with, and takes assignments from, law firms, we solely work with laterally active lawyers and groups.</p>
    <a class="btn" href="#">Read more</a>
  </div>
  <div class="photo" role="img" aria-label="Hand touching a glowing network of contact figures on a dark screen" style="background:linear-gradient(135deg,#5a5a5c,#2a2a2c 55%,#111)"></div>
</section>

<section class="how">
  <h2 class="section-title">How we do it</h2>
  <div class="how-grid">
    <div class="step">
      <svg viewBox="0 0 44 44" fill="none" stroke="#333" stroke-width="3"><circle cx="22" cy="22" r="17"/><circle cx="22" cy="22" r="9"/><circle cx="22" cy="22" r="2" fill="#333"/></svg>
      <h3>Goals</h3><p>Unveiling and balancing motivations, needs, and wants, as they surround your move.</p>
    </div>
    <div class="step">
      <svg viewBox="0 0 44 44" fill="none" stroke="#333" stroke-width="3"><circle cx="19" cy="19" r="12"/><path d="M28 28l11 11"/></svg>
      <h3>Research</h3><p>A comprehensive research initiative to vet the entire market.</p>
    </div>
    <div class="step">
      <svg viewBox="0 0 44 44" fill="#333"><rect x="12" y="34" width="20" height="6"/><rect x="16" y="14" width="12" height="20"/><rect x="13" y="4" width="18" height="10"/></svg>
      <h3>Strategy</h3><p>We work together to assess our market of interest, and create a realistic plan.</p>
    </div>
    <div class="step">
      <svg viewBox="0 0 44 44" fill="#333"><path d="M6 17h8l20-10v30L14 27H6z"/><rect x="12" y="27" width="6" height="11"/></svg>
      <h3>Marketing materials</h3><p>develop a dossier and business and integration plan for you, as they surround your experience.</p>
    </div>
    <div class="step">
      <svg viewBox="0 0 44 44" fill="none" stroke="#333" stroke-width="3"><path d="M4 18l10-8 8 6 8-6 10 8M10 24l8 8 4-4 4 4 8-8"/></svg>
      <h3>The approach</h3><p>Of vital importance to you, as a default, I approach the chair or managing partner.</p>
    </div>
    <div class="step">
      <svg viewBox="0 0 44 44" fill="none" stroke="#333" stroke-width="3"><path d="M6 8h24v16H16l-6 6v-6H6z"/><path d="M34 16h4v16h-4v5l-6-5H18v-4"/></svg>
      <h3>Discussions</h3><p>I prepare you for, and facilitate, ongoing discussions between you and the firm.</p>
    </div>
    <div class="step">
      <svg viewBox="0 0 44 44" fill="#333"><circle cx="22" cy="12" r="6"/><path d="M12 36c0-8 4-14 10-14s10 6 10 14z"/><circle cx="9" cy="18" r="4"/><circle cx="35" cy="18" r="4"/></svg>
      <h3>Vetting the players</h3><p>I am fully involved in vetting the active field as the process unfolds. When you factor in my experience.</p>
    </div>
    <div class="step">
      <svg viewBox="0 0 44 44" fill="#333"><circle cx="22" cy="10" r="6"/><path d="M12 30c0-8 4-12 10-12s10 4 10 12z"/><rect x="8" y="32" width="28" height="6"/></svg>
      <h3>Negotiations</h3><p>Once we've arrived at a point of decision, I negotiate the finer details of your compensation and contract.</p>
    </div>
    <div class="step">
      <svg viewBox="0 0 44 44" fill="none" stroke="#333" stroke-width="3"><path d="M22 3l5 4 6-1 2 6 5 4-3 6 3 6-5 4-2 6-6-1-5 4-5-4-6 1-2-6-5-4 3-6-3-6 5-4 2-6 6 1z"/><path d="M15 22l5 5 9-10"/></svg>
      <h3>Ultimate decision and transition</h3><p>I work with you on making the final decision, constructing and executing.</p>
    </div>
  </div>
  <a class="btn" href="#">Read more</a>
</section>

<section class="different">
  <div class="different-text">
    <h2 class="section-title">Why we are different</h2>
    <p>Lateral placement is our chosen profession. We are not failed attorneys who are trying our hand at recruitment – this is our strong ground, and we pride ourselves on knowing more about the business of law than anyone else in our profession.</p>
    <p>We do not, under any circumstances, take mandates from a law firm. This means that there is no conflict of interest between us and the partners that we represent.</p>
    <a class="btn" href="#">Read more</a>
  </div>
  <div class="photo" role="img" aria-label="Colleagues shaking hands across a meeting table" style="background:linear-gradient(135deg,#9fb3c6,#4c5866 55%,#22262c)"></div>
</section>

<section class="founder">
  <div class="photo" role="img" aria-label="Portrait of the founder in a suit and tie in a bright office" style="background:linear-gradient(135deg,#e2e2e2,#9a9a9a 55%,#4a4a4a)"></div>
  <div class="founder-text">
    <h2 class="section-title">About our founder</h2>
    <p>My profession is BigLaw search and placement. I am also an author (Bar Quill Press), speaker, and Telvane and Civic Counsel Media contributor. I've previously worked in-house with the likes of Harrow &amp; Finch, Starloom Pictures and others. Along with my Telvane and Civic Counsel columns, I can be found in the Daily Ledger, Vantage News Weekly, Counselnote, Meridian Broadcast, The World Bar Journal, Market Insight, Careerhub.example, among others.</p>
    <a class="btn" href="#">Read more</a>
  </div>
</section>

<section class="blog">
  <h2 class="section-title">Latest blog</h2>
  <svg class="arrow left" width="18" height="30" viewBox="0 0 18 30"><path d="M15 3L4 15l11 12" fill="none" stroke="#444" stroke-width="4"/></svg>
  <svg class="arrow right" width="18" height="30" viewBox="0 0 18 30"><path d="M3 3l11 12L3 27" fill="none" stroke="#444" stroke-width="4"/></svg>
  <div class="blog-post">
    <div class="photo" role="img" aria-label="Interviewer holding a microphone toward a guest outdoors" style="background:linear-gradient(135deg,#c9c2b8,#7d7468 55%,#3b352f)"></div>
    <div class="post-body">
      <div class="post-title">Telvane interviews</div>
      <div class="post-meta">NOV 22, 2015 &nbsp;|&nbsp; BY ADMIN</div>
      <p>A candid series of conversations with partners who have made the move, what drove their decision, how the process unfolded, and what they would tell colleagues weighing a similar step. Each interview looks at timing, culture, compensation and the practical details of a smooth transition between leading firms.</p>
      <a class="btn" href="#">Read more</a>
    </div>
  </div>
</section>

<section class="contact">
  <h2 class="section-title">Contact us</h2>
  <div class="contact-form">
    <div class="field">Your Name</div>
    <div class="field">Email Address</div>
    <div class="field message">Message</div>
    <div class="send">Send message</div>
  </div>
</section>

<footer class="footer">
  <div class="footer-info">
    <span><svg width="14" height="20" viewBox="0 0 14 20"><path d="M7 0a7 7 0 0 0-7 7c0 5 7 13 7 13s7-8 7-13a7 7 0 0 0-7-7z" fill="#ccc"/><circle cx="7" cy="7" r="2.5" fill="#141414"/></svg>418 Halvern Ave. Lakeport, NY 10990</span>
    <span><svg width="18" height="18" viewBox="0 0 18 18"><path d="M4 1l3 4-2 2c1 3 3 5 6 6l2-2 4 3-2 3C8 17 1 10 1 3z" fill="#ccc"/></svg>555.014.2290</span>
    <span><svg width="20" height="14" viewBox="0 0 20 14"><rect width="20" height="14" fill="#ccc"/><path d="M0 0l10 8 10-8" fill="none" stroke="#141414" stroke-width="1.5"/></svg>hello@keystonemeridian.com</span>
  </div>
  <div class="copyright">Copyright © 2015 Company Name. All Rights Reserved</div>
</footer>

</body>
</html>
```